New travel store signage for Brisvale Journeys to attract luxury travellers.

Hello,
We are looking to change the signage of our stores. The signage must include the following:
1. Brisvale Journeys Logo (attached)
2. The text...The Travel & Cruise Experts
3. Brand Colours ( Fb0196, 412266, d41d84 and ffffff)
Please note the signage design must be central and only cover two thirds of the store front. We have also attached an image of one of our new stores which might be helpful when preparing a mock up.

We are looking for a quick turnaround on this, making a decision within 48 hours.

Target Market(s)

Retail

Industry/Entity Type

Travel Agency

Font styles to use
Other font styles liked:
• Radley

Colors
E54698
E96AAD
F1A4CE
F9D9EA
FCEFF6
6B429C
8869AF
B7A5CE
E3DAEB
F3F0F8

Requirements
Must have
• Hello, We are looking to change the signage of our stores. The signage must include the following: 1. Brisvale Journeys Logo (attached) 2. The text...The Travel & Cruise Experts 3. Brand Colours ( Fb0196, 412266, d41d84 and ffffff) Please note the signage design must be central and only cover two thirds of the store front.
Should not have
• different colour or fonts. Gradient design.

```html
<!DOCTYPE html>
<html lang="en">
<head>
<meta charset="UTF-8">
<title>Brisvale Journeys – Store Signage Options</title>
<link rel="stylesheet" href="https://fonts.googleapis.com/css2?family=Radley&family=Roboto:wght@900&display=swap">
<style>
  :root {
    --brand-pink: #e5158f;
    --brand-magenta: #d41d84;
    --brand-purple: #412266;
    --brand-white: #ffffff;
    --frame-line: #c9c9c9;
    --brand-gradient: linear-gradient(90deg, #e8168f 0%, #b0217c 35%, #7a2270 65%, #412266 100%);
  }
  * { margin: 0; padding: 0; box-sizing: border-box; }
  html, body {
    width: 1200px; height: 1200px; overflow: hidden;
    background: var(--brand-white);
  }
  .sheet { position: relative; width: 1200px; height: 1200px; }

  .option-label {
    position: absolute; left: 108px;
    font-family: "Roboto", Arial, sans-serif; font-weight: 900;
    font-size: 31px; letter-spacing: 0.2px;
    color: var(--brand-purple); line-height: 1;
  }

  .sign {
    position: absolute; left: 106px; width: 996px; height: 150px;
    border: 1px solid var(--frame-line);
    background: var(--brand-white); overflow: hidden;
  }
  .sign--gradient { background: var(--brand-gradient); border: none; }

  .wordmark {
    position: absolute;
    font-family: "Radley", Georgia, serif; font-weight: 400;
    color: var(--brand-purple); line-height: 1; white-space: nowrap;
  }
  .wordmark--end { left: 0; text-align: right; }
  .sign--gradient .wordmark { color: var(--brand-white); }

  .divider {
    position: absolute; left: 377px; top: 64px;
    width: 2px; height: 30px; background: var(--brand-purple);
  }
  .sign--gradient .divider { background: var(--brand-white); }

  .tagline {
    position: absolute;
    font-family: "Roboto", Arial, sans-serif; font-weight: 900;
    font-size: 30px; line-height: 1; white-space: nowrap;
    color: var(--brand-purple);
  }
  .sign--gradient .tagline { color: var(--brand-white); }

  .tagline-panel {
    position: absolute; left: 432px; top: 37px;
    width: 564px; height: 74px;
    border-radius: 10px 0 0 10px;
    background: var(--brand-purple);
  }
  .tagline-panel--gradient { background: var(--brand-gradient); }
  .tagline-panel .tagline {
    left: 33px; top: 22px; color: var(--brand-white);
  }
</style>
</head>
<body>
<main class="sheet">

  <h2 class="option-label" style="top:108px">OPTION 1</h2>
  <section class="sign" style="top:158px">
    <span class="wordmark wordmark--end" style="width:347px; top:59px; font-size:34px">Brisvale Journeys</span>
    <span class="divider"></span>
    <span class="tagline" style="left:408px; top:62px">THE TRAVEL &amp; CRUISE EXPERTS</span>
  </section>

  <h2 class="option-label" style="top:377px">OPTION 2</h2>
  <section class="sign sign--gradient" style="top:431px">
    <span class="wordmark wordmark--end" style="width:347px; top:59px; font-size:34px">Brisvale Journeys</span>
    <span class="divider"></span>
    <span class="tagline" style="left:408px; top:62px">THE TRAVEL &amp; CRUISE EXPERTS</span>
  </section>

  <h2 class="option-label" style="top:652px">OPTION 3</h2>
  <section class="sign" style="top:700px">
    <span class="wordmark" style="left:140px; top:70px; font-size:29px">Brisvale Journeys</span>
    <div class="tagline-panel">
      <span class="tagline">THE TRAVEL &amp; CRUISE EXPERTS</span>
    </div>
  </section>

  <h2 class="option-label" style="top:923px">OPTION 4</h2>
  <section class="sign" style="top:972px">
    <span class="wordmark wordmark--end" style="width:391px; top:50px; font-size:42px">Brisvale Journeys</span>
    <div class="tagline-panel tagline-panel--gradient">
      <span class="tagline">THE TRAVEL &amp; CRUISE EXPERTS</span>
    </div>
  </section>

</main>
</body>
</html>
```